Domain Parking page and Listing page

1)
In need a design of a domain parking page, mainly with the same features as KOV.example as can be seen here: https://pickturnip.example/

2)
I need a design of a website with all domains listed. There's no company logo/name yet so it should be in plain font, for example "lotsbrim.example" (this is just an example), similar as:
https://kov.example/search?&terms=park&results=50&order_by=relevance

Delivery after approval in HTML/CSS. Should be responsive. Ideally use a framework like Bootstrap

Target Market(s)

Domain buyers, business owners

Industry/Entity Type

Business to business, Marketing, domains

Coding

Coded - Design and coding required

Number of Pages Required

2 page

Font styles to use
Sans Serif

Requirements
Must have
• Responsive design, worldly design.

```html
<!DOCTYPE html>
<html lang="en">
<head>
<meta charset="utf-8">
<title>plotharbor.example is for sale</title>
<link rel="stylesheet" href="https://fonts.googleapis.com/css2?family=Poppins:wght@600;700&family=Barlow:wght@400;500;600&display=swap">
<style>
:root{
  --navy:#0f1836;
  --navy-deep:#0b1230;
  --mint:#3cf4d2;
  --ink:#0b1535;
  --text:#1c1c1c;
  --line:#1f2a44;
  --white:#ffffff;
}
*{box-sizing:border-box;margin:0;padding:0}
html,body{width:1200px;height:2409px;overflow:hidden}
body{font-family:'Barlow',sans-serif;color:var(--text);background:var(--white);position:relative}
.heading{font-family:'Poppins',sans-serif}
.btn{display:inline-flex;align-items:center;justify-content:center;background:var(--mint);color:var(--ink);font-family:'Poppins',sans-serif;font-weight:600;font-size:17px;text-decoration:none;border:none}

/* hero */
.hero{position:absolute;left:0;top:0;width:1200px;height:649px;background:radial-gradient(ellipse at 65% 35%,#1a2650 0%,var(--navy) 55%,var(--navy-deep) 100%)}
.topbar{position:absolute;left:98px;top:20px;right:95px;height:52px;display:flex;align-items:center;color:var(--white)}
.brand{display:flex;align-items:center;gap:10px;white-space:nowrap}
.brand-dot{width:46px;height:46px;background:var(--white);border-radius:10px;flex:none}
.brand-name{font-family:'Poppins',sans-serif;font-weight:600;font-size:26px;color:var(--white);white-space:nowrap}
.brand-sub{border-left:1.5px solid rgba(255,255,255,.7);height:40px;margin-left:6px;padding-left:12px;display:flex;align-items:center;font-family:'Poppins',sans-serif;font-weight:600;font-size:14px;color:var(--white);white-space:nowrap}
.nav{display:flex;gap:24px;margin-left:34px;font-size:17px;font-weight:500}
.nav span{white-space:nowrap}
.login{margin-left:auto;width:108px;height:52px;border:2px solid var(--white);border-radius:4px;display:flex;align-items:center;justify-content:center;font-family:'Poppins',sans-serif;font-weight:600;font-size:18px;flex:none}
.hero-art{position:absolute;left:52px;top:145px;width:320px;height:410px;border-radius:40% 50% 45% 40%;background:radial-gradient(circle,rgba(255,255,255,.22),rgba(120,110,240,.12) 55%,rgba(255,255,255,0) 72%)}
.hero-title{position:absolute;left:320px;top:220px;width:490px;text-align:center;color:var(--white);font-size:43px;font-weight:700;line-height:61px}
.hero-cta{position:absolute;left:496px;top:356px;width:136px;height:47px}
.offer{position:absolute;left:821px;top:173px;width:327px;height:403px;background:var(--white);border-radius:16px;padding:0 27px}
.offer h2{font-size:21px;text-align:center;margin-top:27px;font-weight:600;color:var(--ink)}
.offer-input{margin-top:19px;height:53px;border:1px solid #222;border-radius:3px;padding-left:18px;display:flex;align-items:center;font-size:15px;color:#222}
.offer-next{margin-top:22px;width:271px;height:51px;font-size:18px}
.perks{list-style:none;margin-top:26px;font-size:15.5px}
.perks li{display:flex;align-items:center;gap:18px;height:31px}
.perks em{font-style:normal;color:var(--mint)}
.pay{display:flex;gap:8px;margin-top:19px;margin-left:-5px}
.pay span{width:50px;height:33px;border:1px solid #cfd4dc;border-radius:3px;background:#f3f5f8}

/* features */
.features{position:absolute;left:0;top:649px;width:1200px;height:380px;display:flex;justify-content:center;gap:86px;padding-top:62px;padding-right:90px}
.feature{width:190px;text-align:center;font-size:18px;line-height:31px}
.tile{width:190px;height:176px;border-radius:16px;border:11px solid var(--mint);background:var(--white);display:flex;align-items:center;justify-content:center;margin-bottom:14px}
.tile.dark{border-color:var(--ink)}

/* pitch */
.pitch{position:absolute;left:0;top:1029px;width:1200px;height:418px;background:linear-gradient(180deg,var(--navy) 0%,#111c3c 100%);color:var(--white)}
.pitch h2{position:absolute;left:98px;top:98px;font-size:31px;line-height:41px;font-weight:700}
.pitch p{position:absolute;left:98px;top:190px;width:420px;font-size:16px;line-height:31px}
.pitch .btn{position:absolute;left:100px;top:268px;width:136px;height:47px}
.pitch-art{position:absolute;left:690px;top:22px;width:380px;height:380px;border-radius:50%;background:radial-gradient(circle at 55% 55%,#2a3a5e 0%,#25334f 60%,rgba(37,51,79,.2) 100%)}

/* listing */
.listing{position:absolute;left:0;top:1447px;width:1200px;height:596px}
.listing h2{text-align:center;font-size:31px;font-weight:700;color:var(--text);margin-top:52px}
.rows{position:absolute;left:153px;top:126px;width:894px}
.row{height:62px;border:1px solid var(--line);border-radius:3px;display:flex;align-items:center;padding:0 24px 0 28px;margin-bottom:30px;font-size:16px}
.row .price{margin-left:auto;color:var(--mint);font-size:17px;width:76px}
.row .act{width:109px;height:43px;margin-left:8px;background:var(--ink);color:var(--white);display:flex;align-items:center;justify-content:center;font-weight:600;font-size:17px}
.see{position:absolute;left:519px;top:484px;width:137px;height:48px}

/* footer */
.footer{position:absolute;left:0;top:2043px;width:1200px;height:366px;background:var(--navy);color:var(--white)}
.footer .brand{position:absolute;left:99px;top:68px;gap:7px}
.footer .brand-dot{width:35px;height:35px;border-radius:8px}
.footer .brand-name{font-size:20px}
.footer .brand-sub{height:30px;font-size:11px;padding-left:9px;margin-left:4px}
.follow{position:absolute;left:100px;top:142px;font-size:22px;font-weight:700}
.social{position:absolute;left:102px;top:190px;display:flex;gap:20px}
.social span{width:27px;height:27px;border:2.5px solid var(--white);border-radius:4px}
.col{position:absolute;top:80px;font-size:16px}
.col h3{font-family:'Barlow',sans-serif;font-size:24px;font-weight:500;margin-bottom:10px}
.col li{list-style:none;line-height:31px}
.rule{position:absolute;left:98px;right:98px;top:301px;border-top:1px solid rgba(255,255,255,.8)}
.copy{position:absolute;left:0;width:1200px;top:330px;text-align:center;font-size:16px}
</style>
</head>
<body>

<section class="hero">
  <header class="topbar">
    <div class="brand"><span class="brand-dot"></span><span class="brand-name">KOV.example</span><span class="brand-sub">A Hollowbay Brand</span></div>
    <nav class="nav"><span>Buy a domain</span><span>Sell your domain</span><span>Learn ⌄</span><span>Company ⌄</span></nav>
    <div class="login">Login</div>
  </header>
  <div class="hero-art" role="img" aria-label="Illustration of an astronaut floating beside a browser address bar"></div>
  <h1 class="hero-title heading">plotharbor.example is for sale!</h1>
  <a class="btn hero-cta">Get Started</a>

  <aside class="offer">
    <h2 class="heading">Make an offer</h2>
    <div class="offer-input">My offer in USD</div>
    <a class="btn offer-next">Next</a>
    <ul class="perks">
      <li><svg width="14" height="12" viewBox="0 0 14 12"><path d="M1 6l4 4 8-9" fill="none" stroke="#3cf4d2" stroke-width="2.5"/></svg><span><em>Free</em> Ownership transfer</span></li>
      <li><svg width="14" height="12" viewBox="0 0 14 12"><path d="M1 6l4 4 8-9" fill="none" stroke="#3cf4d2" stroke-width="2.5"/></svg><span><em>Free</em> Transaction support</span></li>
      <li><svg width="14" height="12" viewBox="0 0 14 12"><path d="M1 6l4 4 8-9" fill="none" stroke="#3cf4d2" stroke-width="2.5"/></svg><span>Secure payments</span></li>
    </ul>
    <div class="pay"><span></span><span></span><span></span><span></span><span></span></div>
  </aside>
</section>

<section class="features">
  <div class="feature">
    <div class="tile"><svg width="78" height="90" viewBox="0 0 78 90"><path d="M39 3L6 15v25c0 22 15 38 33 46 18-8 33-24 33-46V15z" fill="none" stroke="#0b1535" stroke-width="3"/><path d="M24 44l11 11 21-22" fill="none" stroke="#3cf4d2" stroke-width="5"/></svg></div>
    Buyer Protection<br>program
  </div>
  <div class="feature">
    <div class="tile dark"><svg width="96" height="86" viewBox="0 0 96 86"><rect x="2" y="2" width="46" height="58" fill="none" stroke="#3cf4d2" stroke-width="3"/><rect x="48" y="24" width="46" height="60" fill="none" stroke="#0b1535" stroke-width="3"/><path d="M60 36H28l8-8M36 54h32l-8 8" fill="none" stroke="#0b1535" stroke-width="3"/></svg></div>
    Fast &amp; easy<br>transfers
  </div>
  <div class="feature">
    <div class="tile"><svg width="96" height="90" viewBox="0 0 96 90"><circle cx="54" cy="22" r="19" fill="none" stroke="#0b1535" stroke-width="3"/><text x="54" y="30" text-anchor="middle" font-family="Barlow,sans-serif" font-size="22" font-weight="600" fill="#0b1535">$</text><path d="M4 72l16-16h22c5 0 5 8 0 8H30M46 64l28-14c8-4 12 4 6 8L50 78H24l-8 10z" fill="none" stroke="#3cf4d2" stroke-width="3"/></svg></div>
    Hassle free<br>payments
  </div>
</section>

<section class="pitch">
  <h2 class="heading">The simple, safe way<br>to buy domain names</h2>
  <p>No matter what kind of domain you want to buy, we make the transfer simple and safe.</p>
  <a class="btn">Get Started</a>
  <div class="pitch-art" role="img" aria-label="Illustration of a person at a laptop holding up a browser address bar"></div>
</section>

<section class="listing">
  <h2 class="heading">Explore other popular domains from the seller</h2>
  <div class="rows">
    <div class="row"><span>quillnest.example</span><span class="price">$8,590</span><span class="act">BUY</span></div>
    <div class="row"><span>vorlin.example</span><span class="price">$69,900</span><span class="act">BUY</span></div>
    <div class="row"><span>pantrynotes.example</span><span class="price">$8,590</span><span class="act">Make Offer</span></div>
    <div class="row"><span>mizzle.example</span><span class="price">$8,590</span><span class="act">Make Offer</span></div>
  </div>
  <a class="btn see">See More</a>
</section>

<footer class="footer">
  <div class="brand"><span class="brand-dot"></span><span class="brand-name">KOV.example</span><span class="brand-sub">A Hollowbay Brand</span></div>
  <div class="follow heading">Follow us</div>
  <div class="social"><span></span><span></span><span></span><span></span></div>
  <div class="col" style="left:415px"><h3>Services</h3><ul><li>Buy a domain</li><li>Sell your domain</li><li>API Partnership Program</li><li>Brokerage</li></ul></div>
  <div class="col" style="left:668px"><h3>Learn</h3><ul><li>News</li><li>Trust &amp; Security</li><li>Help center</li><li>Transaction explorer</li></ul></div>
  <div class="col" style="left:920px"><h3>Company</h3><ul><li>Careers – We’re hiring!</li><li>Our story</li><li>Contact us</li></ul></div>
  <div class="rule"></div>
  <div class="copy">Copyrights@2023.KOV.example.All Rights Reserved</div>
</footer>

</body>
</html>
```